Redesign Website - Current one too plain

The description is in the uploaded file. Please let me know if you need any more information. I'd prefer it if someone could implement the design to a WordPress site but the best design will win, regardless.
I would like the forms to look nice as well
UPDATE:
I don't think we can use the images that I provided, I think they make the site look a bit 'cheap' and I really don't know how to replace them. One thought I have had is to make the "Simple, Unique, Effective" a second feature on the right side of the page with the search on the left
Target Market(s)
Small companies, private sellers of cars and people who rent their caravan/holiday home out
Industry/Entity Type
Advertising
Number of Pages Required
3 page
Colors
Designer to choose colors to be used in the design.
Look and feel

```html
<!DOCTYPE html>
<html lang="en">
<head>
<meta charset="utf-8">
<title>KODIQ – Simple. Unique. Effective.</title>
<link rel="stylesheet" href="https://fonts.googleapis.com/css2?family=Poppins:ital,wght@0,400;0,500;0,600;0,700;0,800;0,900;1,400&display=swap">
<style>
:root{
  --blue:#1b6fd0;
  --ink:#262626;
  --yellow:#f2d100;
  --yellow-soft:#f9fdd5;
  --hero-top:#f7fbff;
  --hero-bottom:#dcebff;
  --grey:#f1f1f1;
  --muted:#555;
  --line:#8a8a8a;
}
*{box-sizing:border-box;margin:0;padding:0}
html,body{width:1200px;height:3378px;overflow:hidden}
body{position:relative;font-family:'Poppins',sans-serif;color:var(--ink);background:#fff}
.abs{position:absolute}
.brand{font-family:'Poppins',sans-serif;font-weight:500;font-size:28px;letter-spacing:3px;color:var(--blue);display:flex;align-items:center;gap:10px}
.brand .dot{width:22px;height:22px;border-radius:50%;background:var(--blue)}
.brand.footer{color:#777}
.brand.footer .dot{background:#777}

.hero{left:0;top:0;width:1200px;height:789px;background:linear-gradient(160deg,var(--hero-top) 0%,#eef5ff 45%,var(--hero-bottom) 100%)}
.nav{right:75px;top:38px;display:flex;align-items:center;gap:38px;font-weight:600;font-size:16px}
.nav .login{border:2px solid var(--blue);color:var(--blue);border-radius:22px;padding:7px 16px}
.tagline{left:73px;top:268px;font-size:39px;font-weight:500;color:var(--blue);word-spacing:10px;white-space:nowrap;z-index:2}
.plate{left:72px;top:320px;font-size:128px;font-weight:800;line-height:1;letter-spacing:20px;z-index:2}
.arrows{left:80px;top:455px;display:flex;gap:26px;z-index:2}
.pills{left:75px;top:529px;display:flex;gap:8px;z-index:2}
.pill{background:var(--blue);color:#fff;font-size:14px;height:42px;border-radius:21px;display:flex;align-items:center;justify-content:center;padding:0 15px}
.btn{background:var(--yellow);color:#fff;font-weight:600;display:flex;align-items:center;justify-content:center;border-radius:30px}
.search{left:75px;top:596px;width:178px;height:56px;font-size:19px;font-weight:500}
.vehicles{left:374px;top:269px}

.card{top:860px;width:328px;height:451px;background:#fff;border-radius:10px;box-shadow:0 2px 12px rgba(0,0,0,.12);border-bottom:6px solid var(--yellow);text-align:center}
.card .blob{position:absolute;left:44px;top:22px;width:240px;height:240px;border-radius:50%;background:var(--yellow-soft)}
.card svg.icon{position:absolute;left:124px;top:100px}
.card h3{position:absolute;top:276px;width:100%;font-size:34px;font-weight:700;color:var(--blue)}
.card p{position:absolute;top:330px;left:30px;right:30px;font-size:15.5px;line-height:28px;color:#333}

.eyebrow{font-size:30px;font-weight:500;color:var(--blue)}
.display{font-weight:900;line-height:1}
.about-eyebrow{left:75px;top:1420px}
.welcome{left:72px;top:1470px;font-size:104px}
.welcome .accent{color:var(--yellow);display:block;margin-top:2px}
.about-text{left:75px;top:1705px;width:520px;font-size:18px;line-height:37px;color:#333}
.learn{left:75px;top:1889px;width:194px;height:62px;font-size:20px;font-weight:700}
.about-photo{left:610px;top:1429px;width:517px;height:524px;border-radius:46% 54% 42% 58%/52% 40% 60% 48%;background:linear-gradient(160deg,#cfd9e2 0%,#e9e4d7 45%,#7f9868 100%)}

.testi-band{left:0;top:2040px;width:1200px;height:326px}
.review-eyebrow{right:73px;top:2030px}
.testi-title{right:73px;top:2080px;font-size:104px}
.quote{top:2202px;width:328px;height:276px;background:#fff;border-radius:10px;box-shadow:0 2px 12px rgba(0,0,0,.12);padding:38px 24px 0}
.quote .mark{position:absolute;left:14px;top:8px;font-size:90px;line-height:1;font-weight:900;color:#f7e98a;font-family:'Poppins',sans-serif}
.quote p{position:relative;font-style:italic;font-size:15.5px;line-height:27.5px;color:#333}
.quote h4{position:relative;margin-top:10px;font-size:17px;font-weight:600;color:var(--blue)}

.contact-bg{left:0;top:2566px;width:1200px;height:607px;background:linear-gradient(180deg,#ececec 0%,#e4e2dd 60%,#ddd6c6 100%)}
.contact-eyebrow{left:0;width:1200px;top:2630px;text-align:center}
.contact-title{left:0;width:1200px;top:2672px;text-align:center;font-size:104px}
.field-label{font-size:15px;color:#333}
.field-line{height:1px;background:var(--line)}
.submit{left:503px;top:3039px;width:193px;height:62px;font-size:20px;font-weight:700}

.copyright{left:75px;top:3285px;font-size:14px;line-height:28px;color:#666}
.social{left:886px;top:3262px;display:flex;gap:30px}
.social span{width:26px;height:26px;border-radius:50%;background:var(--yellow)}
</style>
</head>
<body>

<section class="hero abs" aria-label="Hero"></section>
<div class="brand abs" style="left:75px;top:42px"><span class="dot"></span>KODIQ</div>
<nav class="nav abs"><span>Home</span><span>Advertise</span><span>Contact</span><span>Register</span><span class="login">Login</span></nav>

<svg class="vehicles abs" width="826" height="472" viewBox="0 0 826 472" role="img" aria-label="Silver SUV, static caravan and van, each with a yellow code tag">
  <defs>
    <linearGradient id="vehicleTone" x1="0" y1="0" x2="1" y2="1">
      <stop offset="0" stop-color="#d8dbe0"/>
      <stop offset="0.5" stop-color="#a9adb3"/>
      <stop offset="1" stop-color="#c9ced6"/>
    </linearGradient>
  </defs>
  <path d="M330 0H826V472H300Q270 472 270 442V330H30Q0 330 0 300V170Q0 140 30 140H300V30Q300 0 330 0Z" fill="url(#vehicleTone)"/>
</svg>

<div class="tagline abs">Simple. Unique. Effective.</div>
<div class="plate abs">A1</div>
<div class="arrows abs">
  <svg width="24" height="34" viewBox="0 0 24 34"><path d="M18 4 6 17l12 13" fill="none" stroke="#222" stroke-width="3"/></svg>
  <svg width="24" height="34" viewBox="0 0 24 34"><path d="M6 4l12 13L6 30" fill="none" stroke="#222" stroke-width="3"/></svg>
  <svg width="24" height="34" viewBox="0 0 24 34"><path d="M18 4 6 17l12 13" fill="none" stroke="#222" stroke-width="3"/></svg>
  <svg width="24" height="34" viewBox="0 0 24 34"><path d="M6 4l12 13L6 30" fill="none" stroke="#222" stroke-width="3"/></svg>
</div>
<div class="pills abs"><span class="pill" style="width:90px">Car</span><span class="pill">Caravan</span><span class="pill">Company</span></div>
<div class="btn search abs">Search</div>

<article class="card abs" style="left:75px">
  <div class="blob"></div>
  <svg class="icon" width="80" height="80" viewBox="0 0 80 80" fill="none" stroke="#111" stroke-width="2.5"><path d="M40 6a24 24 0 0 0-14 43c3 3 4 6 4 10h20c0-4 1-7 4-10A24 24 0 0 0 40 6z"/><path d="M30 64h20M32 70h16M36 76h8M30 30c4 4 8-4 10 0s6 4 10 0"/></svg>
  <h3>Simple</h3>
  <p>Create  your advert and display your code</p>
</article>
<article class="card abs" style="left:437px">
  <div class="blob"></div>
  <svg class="icon" width="80" height="80" viewBox="0 0 80 80" fill="none" stroke="#111" stroke-width="2.5"><path d="M14 40a24 24 0 0 1 44-13M20 54a20 20 0 0 1-2-14M28 60c-4-6-5-12-4-20a14 14 0 0 1 26-4M36 64c-4-8-4-16-2-22"/><circle cx="54" cy="50" r="12"/><path d="M63 59l12 12"/></svg>
  <h3>Unique</h3>
  <p>Customers find you by an easy-to-remember code</p>
</article>
<article class="card abs" style="left:798px">
  <div class="blob"></div>
  <svg class="icon" width="80" height="80" viewBox="0 0 80 80" fill="none" stroke="#111" stroke-width="2.5"><path d="M22 38h10l8-18c4-4 8 0 6 6l-4 12h16c5 0 6 6 2 8 4 2 3 8-1 8 3 2 2 8-2 8H32l-10-4z"/><rect x="8" y="36" width="14" height="34"/><rect x="58" y="46" width="10" height="26"/><path d="M14 14l3 3M10 24h4M24 8v4"/></svg>
  <h3>Effective</h3>
  <p>Customers are directed to you and not a list of your competitors</p>
</article>

<div class="eyebrow about-eyebrow abs">About Us</div>
<h1 class="display welcome abs">Welcome<span class="accent">KODIQ</span></h1>
<p class="about-text abs">Nemo enim ipsam voluptatem quia voluptas sit aspernatur aut odit  aut fugit, sed quia consequuntur magni dolores eos qui ratione voluptatem sequi nesciunt. Nam libero tempore, cum soluta nobis.</p>
<div class="btn learn abs">Learn More</div>
<div class="about-photo abs" role="img" aria-label="Row of static holiday caravans on a grassy park under a cloudy sky"></div>

<svg class="testi-band abs" width="1200" height="326" viewBox="0 0 1200 326"><path d="M0 0H505q14 0 20 14L640 326H0z" fill="var(--grey)"/></svg>
<div class="eyebrow review-eyebrow abs">Customer Review</div>
<h2 class="display testi-title abs">Testimonials</h2>
<article class="quote abs" style="left:75px"><span class="mark">“</span><p>Nam libero tempore, cum soluta nobis est eligendi optio cumque nihil impedit quo minus  debitis aut rerum necessitatibus saepe eveniet ut et voluptates repudiandae sint et molestiae non recusandae..”</p><h4>Name Heading</h4></article>
<article class="quote abs" style="left:437px"><span class="mark">“</span><p>Nam libero tempore, cum soluta nobis est eligendi optio cumque nihil impedit quo minus  debitis aut rerum necessitatibus saepe eveniet ut et voluptates repudiandae sint et molestiae non recusandae..”</p><h4>Name Heading</h4></article>
<article class="quote abs" style="left:798px"><span class="mark">“</span><p>Nam libero tempore, cum soluta nobis est eligendi optio cumque nihil impedit quo minus  debitis aut rerum necessitatibus saepe eveniet ut et voluptates repudiandae sint et molestiae non recusandae..”</p><h4>Name Heading</h4></article>

<section class="contact-bg abs" role="img" aria-label="Faded photo of a white motorhome parked in a mountain landscape"></section>
<div class="eyebrow contact-eyebrow abs">Get in Touch</div>
<h2 class="display contact-title abs">Contact Us</h2>
<span class="field-label abs" style="left:254px;top:2818px">Name</span>
<span class="field-label abs" style="left:616px;top:2818px">Email</span>
<div class="field-line abs" style="left:254px;top:2864px;width:332px"></div>
<div class="field-line abs" style="left:616px;top:2864px;width:329px"></div>
<span class="field-label abs" style="left:254px;top:2887px">Message</span>
<div class="field-line abs" style="left:254px;top:2998px;width:691px"></div>
<div class="btn submit abs">Submit</div>

<div class="brand footer abs" style="left:75px;top:3228px"><span class="dot"></span>KODIQ</div>
<p class="copyright abs">© Copyright 2023 Company Name.<br>All Rights Reserved.</p>
<div class="social abs" aria-label="Social links"><span></span><span></span><span></span><span></span><span></span></div>

</body>
</html>
```